Facebook page needs a new logo for a business that sells preloved kids clothing

We need a banner to suit a facebook page for our business called "Bright Sprout Apparel". We would like it to be colourful with a childlike theme to it while at the same time looking professional and something that will stand out and catch the eye. We would like the words "Bright Sprout Apparel" used in the banner with the words "Approved by mothers" as the catch phrase in smaller writing.

Industry/Entity Type

Clothing

```html
<!DOCTYPE html>
<html lang="en">
<head>
<meta charset="utf-8">
<title>Bright Sprout Apparel – Cover Banner</title>
<link rel="stylesheet" href="https://fonts.googleapis.com/css2?family=Mystery+Quest&family=Shadows+Into+Light+Two&display=swap">
<style>
  :root {
    --band-top-a: #b8324a;
    --band-top-b: #6f4aa0;
    --sun-yellow: #ffe500;
    --sun-yellow-deep: #f7d000;
    --sea-blue: #1e8fc4;
    --sea-blue-deep: #0f6a93;
    --olive-glow: #6d6a1e;
    --kid-orange: #f07a1a;
    --kid-green: #4f9a12;
    --ink: #1c1c1c;
    --profile-green: #8cc63f;
    --paper: #ffffff;
  }
  * { box-sizing: border-box; margin: 0; padding: 0; }
  html, body { width: 1200px; height: 575px; overflow: hidden; background: var(--paper); }
  .banner { position: relative; width: 1200px; height: 575px; overflow: hidden; background: var(--paper); }

  .pattern-top {
    position: absolute; left: 0; top: 0; width: 1200px; height: 70px;
    background: linear-gradient(90deg, var(--band-top-a), var(--band-top-b) 50%, var(--band-top-a));
  }
  .pattern-sea {
    position: absolute; left: 0; top: 262px; width: 1200px; height: 182px;
    background:
      radial-gradient(ellipse 360px 150px at 560px 90px, var(--olive-glow), transparent 75%),
      linear-gradient(180deg, var(--sea-blue), var(--sea-blue-deep));
  }
  .sun-band { position: absolute; left: 0; top: 36px; width: 1200px; height: 250px; }

  .kid { position: absolute; }
  .kid-left { left: 10px; top: 70px; width: 120px; height: 185px; background: linear-gradient(180deg, var(--kid-orange), #e35a10); border-radius: 50px 50px 20px 20px; opacity: .9; }
  .kid-right { left: 1095px; top: 135px; width: 95px; height: 135px; background: linear-gradient(180deg, var(--kid-green), #3d7d0c); border-radius: 45px 45px 20px 20px; opacity: .9; }

  .title {
    position: absolute; left: 145px; top: 122px; width: 940px;
    text-align: center; white-space: nowrap;
    font-family: "Mystery Quest", cursive; font-weight: 400;
    font-size: 92px; line-height: 1; color: var(--ink);
  }

  .tagline {
    position: absolute; left: 330px; top: 302px;
    font-family: "Shadows Into Light Two", cursive; font-size: 58px; color: var(--paper);
    text-shadow: 2px 2px 0 var(--ink), -1px -1px 0 var(--ink), 1px -1px 0 var(--ink), -1px 1px 0 var(--ink);
    white-space: nowrap;
  }

  .profile {
    position: absolute; left: 31px; top: 299px; width: 241px; height: 235px;
    background: var(--profile-green); border: 5px solid var(--paper);
    box-shadow: 0 0 0 1px #c9c9c9;
    display: flex; align-items: center; justify-content: center; text-align: center;
    font-family: "Mystery Quest", cursive; font-weight: 400; font-size: 38px; line-height: 1.05; color: var(--paper);
    padding: 20px;
  }
</style>
</head>
<body>
  <main class="banner">
    <div class="pattern-top" role="img" aria-label="Colourful circular pattern in red, purple and teal"></div>
    <div class="pattern-sea" role="img" aria-label="Blue wheel-shaped pattern with a soft olive glow in the centre"></div>

    <svg class="sun-band" viewBox="0 0 1200 250" role="img" aria-label="Bright yellow band with red hand-drawn hatching and torn edges" preserveAspectRatio="none">
      <polygon fill="var(--sun-yellow)" points="0,18 60,8 130,22 210,6 300,20 380,4 470,18 560,8 650,22 740,6 830,18 920,4 1010,20 1100,8 1200,16 1200,232 1120,244 1030,226 940,240 850,224 760,246 670,228 580,242 490,226 400,244 310,228 220,242 130,226 60,240 0,230"/>
      <rect x="0" y="60" width="1200" height="130" fill="var(--sun-yellow-deep)" opacity=".45"/>
    </svg>

    <div class="kid kid-left" role="img" aria-label="Orange silhouette of a child jumping"></div>
    <div class="kid kid-right" role="img" aria-label="Green silhouette of a child leaping"></div>

    <h1 class="title">Bright Sprout Apparel</h1>

    <p class="tagline">Approved by mothers</p>

    <div class="profile">Bright Sprout Apparel</div>
  </main>
</body>
</html>
```